Architectural firm needs a graphic representation of our Master Planning process

We need an image to convey our 3-phase, 8-step Master Planning process that we utilize when designing plans for schools K-12. What we currently use looks very outdated in both the design and color scheme. We'd like an EPS created that can be scaled without distortion. The files I've attached show the current graphic and an instruction sheet which also contains our colors.

```html
<!DOCTYPE html>
<html lang="en">
<head>
<meta charset="utf-8">
<title>The Masterplanning Process in Architectural Design</title>
<link rel="stylesheet" href="https://fonts.googleapis.com/css2?family=Montserrat:wght@400;500;600;700&display=swap">
<style>
  :root {
    --backdrop: #d6d7dc;
    --paper: #ffffff;
    --purple: #b98ad8;
    --purple-line: #b89ad6;
    --red: #d41f42;
    --red-text: #b0063a;
    --red-band: #d9485c;
    --teal: #25c0c8;
    --teal-band: #74d8dd;
    --green: #66d62a;
    --green-band: #8ee05a;
    --lime: #b5f01c;
    --ink: #555559;
    --ornament: #eeeef1;
  }
  html, body {
    margin: 0;
    width: 1200px;
    height: 1200px;
    overflow: hidden;
    background: var(--backdrop);
    font-family: "Montserrat", sans-serif;
  }
  .poster {
    position: absolute;
    left: 279px;
    top: 19px;
    width: 642px;
    height: 1162px;
    background: var(--paper);
  }
  .poster svg { display: block; }
  .title { font-size: 16px; font-weight: 600; letter-spacing: 3.4px; fill: var(--ink); }
  .pill-label { font-size: 16px; font-weight: 600; letter-spacing: 2px; fill: #fff; }
  .party { font-size: 16px; font-weight: 700; letter-spacing: 1.6px; }
  .party-school { fill: var(--teal); }
  .party-arch { fill: var(--red-text); }
  .party-fund { fill: var(--green); }
  .step { font-size: 16px; font-weight: 600; letter-spacing: 2px; fill: var(--ink); }
  .note { font-size: 12.4px; font-weight: 400; fill: var(--ink); }
  .legend { font-size: 12.5px; font-weight: 700; letter-spacing: 1px; }
  .icon-line { fill: none; stroke: #fff; stroke-width: 1.6; stroke-linecap: round; stroke-linejoin: round; }
  .glyph { fill: none; stroke: var(--ink); stroke-width: 1.3; stroke-linecap: round; stroke-linejoin: round; }
</style>
</head>
<body>
<div class="poster">
<svg width="642" height="1162" viewBox="0 0 642 1162" xmlns="http://www.w3.org/2000/svg">
  <!-- heading -->
  <text class="title" x="321" y="52" text-anchor="middle">THE MASTERPLANNING PROCESS</text>
  <text class="title" x="321" y="69" text-anchor="middle">IN ARCHITECTURAL DESIGN</text>

  <!-- start marker -->
  <line x1="151" y1="128" x2="251" y2="128" stroke="var(--purple-line)" stroke-width="2"/>
  <line x1="391" y1="128" x2="491" y2="128" stroke="var(--purple-line)" stroke-width="2"/>
  <rect x="278" y="115" width="86" height="27" rx="13.5" fill="var(--purple)"/>
  <text class="pill-label" x="321" y="134" text-anchor="middle">START</text>

  <!-- parties -->
  <text class="party party-school" x="323" y="195" text-anchor="middle">SCHOOL</text>
  <circle cx="321" cy="224" r="22" fill="var(--teal)"/>
  <text class="party party-arch" x="142" y="240" text-anchor="middle">ARCHITECTURAL</text>
  <text class="party party-arch" x="142" y="257" text-anchor="middle">CONSULTANT</text>
  <circle cx="141" cy="287" r="22" fill="var(--red-text)"/>
  <text class="party party-fund" x="500" y="240" text-anchor="middle">FUND RAISING</text>
  <text class="party party-fund" x="500" y="257" text-anchor="middle">CONSULTANT</text>
  <circle cx="500" cy="287" r="22" fill="var(--green)"/>

  <!-- converging bands -->
  <path d="M178 286 H296 Q312 286 312 302 V330" fill="none" stroke="var(--red-band)" stroke-width="16"/>
  <polygon points="177,277 186,286 177,295" fill="var(--paper)"/>
  <path d="M464 286 H346 Q330 286 330 302 V330" fill="none" stroke="var(--green-band)" stroke-width="16"/>
  <polygon points="465,277 456,286 465,295" fill="var(--paper)"/>
  <rect x="313" y="252" width="16" height="76" fill="var(--teal-band)"/>
  <polygon points="313,252 321,260 329,252" fill="var(--paper)"/>
  <polygon points="282,326 360,326 321,374" fill="var(--teal-band)"/>
  <polygon points="282,326 333,326 307,356" fill="var(--red-band)" opacity="0.7"/>
  <polygon points="309,326 360,326 335,356" fill="var(--green-band)" opacity="0.7"/>
  <polygon points="311,326 331,326 321,340" fill="#f5c95a"/>

  <!-- process connectors -->
  <polyline points="321,418 278,490 321,562 364,490 321,418" fill="none" stroke="var(--purple)" stroke-width="4"/>
  <line x1="321" y1="562" x2="321" y2="846" stroke="var(--purple)" stroke-width="4"/>

  <!-- shared steps -->
  <g class="node-shared">
    <circle cx="321" cy="418" r="28" fill="var(--purple)"/>
    <circle cx="321" cy="405" r="10" fill="#1fe0e8"/>
    <circle cx="310" cy="426" r="10" fill="var(--red)"/>
    <circle cx="332" cy="426" r="10" fill="var(--lime)"/>
  </g>
  <g class="node-shared">
    <circle cx="321" cy="703" r="28" fill="var(--purple)"/>
    <circle cx="321" cy="690" r="10" fill="#1fe0e8"/>
    <circle cx="310" cy="711" r="10" fill="var(--red)"/>
    <circle cx="332" cy="711" r="10" fill="var(--lime)"/>
  </g>
  <g class="node-shared">
    <circle cx="321" cy="846" r="28" fill="var(--purple)"/>
    <circle cx="321" cy="833" r="10" fill="#1fe0e8"/>
    <circle cx="310" cy="854" r="10" fill="var(--red)"/>
    <circle cx="332" cy="854" r="10" fill="var(--lime)"/>
  </g>

  <!-- architect steps -->
  <g class="node-arch">
    <circle cx="278" cy="490" r="28" fill="var(--purple)"/>
    <circle cx="278" cy="490" r="23" fill="var(--red)"/>
    <circle class="icon-line" cx="278" cy="490" r="13"/>
    <path class="icon-line" d="M270 494 V487 L278 481 L286 487 V494 Z"/>
    <rect class="icon-line" x="275.5" y="487.5" width="5" height="4"/>
    <line class="icon-line" x1="287" y1="499" x2="292" y2="504"/>
  </g>
  <g class="node-arch">
    <circle cx="364" cy="490" r="28" fill="var(--purple)"/>
    <circle cx="364" cy="490" r="23" fill="var(--red)"/>
    <rect class="icon-line" x="352" y="478" width="10" height="10"/>
    <rect class="icon-line" x="366" y="478" width="10" height="10"/>
    <rect class="icon-line" x="352" y="492" width="10" height="10"/>
    <rect class="icon-line" x="366" y="492" width="10" height="10"/>
  </g>
  <g class="node-arch">
    <circle cx="321" cy="562" r="28" fill="var(--purple)"/>
    <circle cx="321" cy="562" r="23" fill="var(--red)"/>
    <path class="icon-line" d="M313 550 H329 M316 550 V559 L312 566 H330 L326 559 V550 M321 566 V578"/>
  </g>
  <g class="node-arch">
    <circle cx="321" cy="632" r="28" fill="var(--purple)"/>
    <circle cx="321" cy="632" r="23" fill="var(--red)"/>
    <path class="icon-line" d="M316 638 C316 632 311 630 311 624 A10 10 0 0 1 331 624 C331 630 326 632 326 638 Z M317 642 H325 M318 646 H324"/>
  </g>
  <g class="node-arch">
    <circle cx="321" cy="775" r="28" fill="var(--purple)"/>
    <circle cx="321" cy="775" r="23" fill="var(--red)"/>
    <path class="icon-line" d="M312 762 H326 L331 767 V788 H312 Z M326 762 V767 H331 M316 772 H327 M316 777 H327 M316 782 H327"/>
  </g>

  <!-- step glyphs -->
  <g class="glyph-eye">
    <path class="glyph" d="M365 412 V407 H370 M385 407 H392 V412 M392 426 V431 H387 M370 431 H365 V426"/>
    <path class="glyph" d="M367 419 Q378 408 390 419 Q378 430 367 419 Z"/>
    <circle class="glyph" cx="378.5" cy="419" r="4"/>
  </g>
  <g class="glyph-calc">
    <rect class="glyph" x="365" y="689" width="28" height="28"/>
    <path class="glyph" d="M368 695 H374 M382 692 L387 697 M387 692 L382 697 M368 709 H374 M371 706 V712"/>
    <circle class="glyph" cx="386" cy="709" r="6"/>
    <path class="glyph" d="M383 707.5 H389 M383 710.5 H389"/>
  </g>
  <g class="glyph-rocket">
    <path class="glyph" d="M371 852 C374 838 384 832 395 831 C394 842 388 852 374 855 Z"/>
    <circle class="glyph" cx="384" cy="842" r="3"/>
    <path class="glyph" d="M372 846 L366 846 L371 840 L378 839 M380 853 L380 859 L386 854 L387 847 M369 855 L364 860 M365 851 L364 856"/>
  </g>

  <!-- step labels -->
  <text class="step" x="409" y="433">VISIONING</text>
  <text class="step" x="227" y="479" text-anchor="end">PHYSICAL</text>
  <text class="step" x="227" y="496" text-anchor="end">CONDITIONS</text>
  <text class="step" x="227" y="513" text-anchor="end">ASSESSMENT</text>
  <text class="step" x="416" y="479">SPACE</text>
  <text class="step" x="416" y="496" letter-spacing="4">NEEDS</text>
  <text class="step" x="416" y="513">ASSESSMENT</text>
  <text class="step" x="360" y="568">PROBLEM DEFINED</text>
  <text class="step" x="278" y="638" text-anchor="end">IDENTIFY SOLUTIONS</text>
  <text class="step" x="409" y="716">ASSESS AND SELECT</text>
  <text class="step" x="278" y="781" text-anchor="end">COMPLETE REPORT</text>
  <text class="step" x="408" y="858">IMPLEMENT PLAN !</text>

  <!-- finish marker -->
  <line x1="151" y1="929" x2="251" y2="929" stroke="var(--purple-line)" stroke-width="2"/>
  <line x1="391" y1="929" x2="491" y2="929" stroke="var(--purple-line)" stroke-width="2"/>
  <rect x="276" y="916" width="90" height="27" rx="13.5" fill="var(--purple)"/>
  <text class="pill-label" x="321" y="935" text-anchor="middle">FINISH</text>

  <!-- explanatory note -->
  <text class="note" x="87" y="977">Image above depicts a general outline of the process developed by</text>
  <text class="note" x="87" y="991">M&amp;L and used when conducting facilities master plans. The areas of</text>
  <text class="note" x="87" y="1005">responsibility are shown by color yet the groups, especially the school</text>
  <text class="note" x="87" y="1019">and the architect, are always working together towards the goal.</text>

  <!-- legend -->
  <circle cx="119" cy="1038" r="6" fill="var(--teal)"/>
  <text class="legend party-school" x="137" y="1043">BLUE</text>
  <text class="legend party-school" x="202" y="1043">: SCHOOL</text>
  <circle cx="119" cy="1059" r="6" fill="var(--red-text)"/>
  <text class="legend party-arch" x="137" y="1064">RED</text>
  <text class="legend party-arch" x="202" y="1064">: ARCHITECTURAL CONSULTANT</text>
  <circle cx="119" cy="1081" r="6" fill="var(--green)"/>
  <text class="legend party-fund" x="137" y="1086">GREEN</text>
  <text class="legend party-fund" x="202" y="1086">: FUND RAISING CONSULTANT</text>

  <!-- corner decoration area -->
  <rect x="491" y="1006" width="117" height="137" rx="4" fill="var(--ornament)" role="img" aria-label="Decorative line drawing of two faceted crystal shapes"/>
</svg>
</div>
</body>
</html>
```